NEW Modern Sleek Business Card for VR Language Startup

Our startup is using VR to lead the next wave of world language education. We need a two-sided business card that introduces the larger organization (Brightvale Tongues Inc) and our contact info on one side and shows the product, Lexiquorra, on the other side.

Side 1 (contact info)= Brightvale Logo and Contact info (name, title, phone, email)

Side 2 (product)= Lexiquora logo, text, and website
Text= Culturally Immersive Language Learning Games
Website= www.lexiquora-demo.test

Target Market(s)

Education, Technology

Contact Information for Business Card

Contact info will be updated upon approval of the design. For now, put this as a placeholder.

Peter Hallow
Founder & CEO
phallow@mailbox-demo.test
(555)-010-4477

Font styles to use
Other font styles liked:
• Gibson and Century Gothic are the brand fonts

Requirements
Nice to have
• I would love to see cohesion between the design and colors of the two logos. I have attached a few business card designs that I like, so you can get a feel for my preferred style.

```html
<!DOCTYPE html>
<html lang="en">
<head>
<meta charset="utf-8">
<title>Brightvale Tongues – Business Card</title>
<link rel="stylesheet" href="https://fonts.googleapis.com/css2?family=Montserrat:wght@400;500;700&display=swap">
<style>
  :root {
    --page-bg: #2d323c;
    --card-white: #ffffff;
    --grad-teal: #5fc4d6;
    --grad-blue: #63a0cc;
    --grad-violet: #6658ad;
    --ink-dark: #23232a;
    --text-light: #ffffff;
    --accent-coral: #ef5a5f;
  }
  * { box-sizing: border-box; margin: 0; padding: 0; }
  html, body { width: 1200px; height: 900px; overflow: hidden; }
  body {
    background: var(--page-bg);
    font-family: "Montserrat", "Century Gothic", sans-serif;
    position: relative;
  }
  .card {
    position: absolute;
    left: 280px;
    width: 640px;
    height: 366px;
    overflow: hidden;
  }
  .card--front { top: 70px; background: var(--card-white); }
  .card--back {
    top: 464px;
    background: linear-gradient(120deg, var(--grad-teal) 0%, var(--grad-blue) 45%, var(--grad-violet) 100%);
  }

  /* Front */
  .front-panel {
    position: absolute;
    left: 0; top: 0;
    width: 345px; height: 100%;
  }
  .contact-block { position: absolute; left: 62px; top: 100px; color: var(--text-light); }
  .contact-name { font-size: 19px; font-weight: 700; letter-spacing: -0.2px; }
  .contact-title { font-size: 14px; font-weight: 400; margin-top: 4px; }
  .contact-list { list-style: none; margin-top: 56px; }
  .contact-list li {
    display: flex; align-items: center; gap: 11px;
    font-size: 14px; margin-bottom: 10px;
  }
  .contact-icon {
    width: 18px; height: 18px; border-radius: 50%;
    background: var(--text-light);
    display: flex; align-items: center; justify-content: center;
  }
  .brand-mark {
    position: absolute; left: 380px; top: 150px;
    width: 230px;
    display: flex; align-items: center; justify-content: center; gap: 12px;
  }
  .brand-dot { width: 22px; height: 22px; border-radius: 50%; background: var(--accent-coral); }
  .brand-name {
    font-size: 32px; font-weight: 500; letter-spacing: 3px;
    color: var(--ink-dark); text-transform: uppercase;
  }

  /* Back */
  .product-mark {
    position: absolute; left: 110px; top: 150px;
    display: flex; align-items: center; gap: 12px;
    color: var(--text-light);
  }
  .product-dot { width: 20px; height: 20px; border-radius: 50%; background: var(--text-light); }
  .product-name { font-size: 36px; font-weight: 500; letter-spacing: -0.5px; }
  .tagline { position: absolute; left: 330px; top: 140px; color: var(--text-light); }
  .tagline-lead { font-size: 17px; font-weight: 400; }
  .tagline-strong { font-size: 20px; font-weight: 700; margin-top: 2px; }
  .tagline-tail { font-size: 14px; font-weight: 400; margin-top: 3px; }
  .tagline-rule { width: 28px; height: 3px; background: var(--text-light); margin: 24px 0 12px; }
  .product-url { font-size: 14px; letter-spacing: 1.4px; }
</style>
</head>
<body>

<section class="card card--front" aria-label="Business card front">
  <svg class="front-panel" viewBox="0 0 345 366" role="img" aria-label="Gradient panel where the brand head silhouette artwork belongs">
    <defs>
      <linearGradient id="panelGrad" x1="0" y1="0" x2="1" y2="1">
        <stop offset="0" stop-color="#5fb4d2"/>
        <stop offset="0.5" stop-color="#6490c4"/>
        <stop offset="1" stop-color="#6658ad"/>
      </linearGradient>
    </defs>
    <rect width="345" height="366" fill="url(#panelGrad)"/>
  </svg>

  <div class="contact-block">
    <h1 class="contact-name">PETER HALLOW</h1>
    <p class="contact-title">Founder &amp; CEO</p>
    <ul class="contact-list">
      <li>
        <span class="contact-icon">
          <svg width="10" height="10" viewBox="0 0 10 10"><path d="M2 1 L4 1 L4.6 3 L3.5 3.8 Q4.5 5.8 6.2 6.5 L7 5.4 L9 6 L9 8 Q8.5 9 7 9 Q1 8 1 2.5 Q1 1 2 1Z" fill="#6490c4"/></svg>
        </span>
        555.010.4477
      </li>
      <li>
        <span class="contact-icon">
          <svg width="11" height="9" viewBox="0 0 11 9"><rect x="0.8" y="0.8" width="9.4" height="7.4" fill="none" stroke="#6490c4" stroke-width="1.2"/><path d="M1 1 L5.5 5 L10 1" fill="none" stroke="#6490c4" stroke-width="1.2"/></svg>
        </span>
        phallow@mailbox-demo.test
      </li>
      <li>
        <span class="contact-icon">
          <svg width="11" height="11" viewBox="0 0 11 11"><circle cx="5.5" cy="5.5" r="4.6" fill="none" stroke="#6490c4" stroke-width="1.1"/><ellipse cx="5.5" cy="5.5" rx="2" ry="4.6" fill="none" stroke="#6490c4" stroke-width="1"/><line x1="1" y1="5.5" x2="10" y2="5.5" stroke="#6490c4" stroke-width="1"/></svg>
        </span>
        www.hallow-demo.test
      </li>
    </ul>
  </div>

  <div class="brand-mark">
    <span class="brand-dot"></span>
    <span class="brand-name">Brightvale</span>
  </div>
</section>

<section class="card card--back" aria-label="Business card back">
  <div class="product-mark">
    <span class="product-dot"></span>
    <span class="product-name">Lexiquora</span>
  </div>
  <div class="tagline">
    <p class="tagline-lead">Culturally</p>
    <p class="tagline-strong">IMMERSIVE Language</p>
    <p class="tagline-tail">Learning Games</p>
    <div class="tagline-rule"></div>
    <p class="product-url">www.lexiquora-demo.test</p>
  </div>
</section>

</body>
</html>
```